New business card for my lawn and landscape business

Dorrin Yard and Building is a full-service lawn care, landscaping, and light construction company serving Paragould and the Northeast Arkansas region. The business is owned and operated by Marcus Toller, with a reputation for hands-on, detail-oriented service, dependable crews, and quality results for both residential and commercial clients. A well regarded business with great reviews.
Owner Marcus Toller
Dorrinyardandbuilding.example

Target Market(s)

Commercial, Middle, and upper class in north east Arkansas

Industry/Entity Type

Lawn maintenance and landscape

Contact Information for Business Card

Dorrin Yard And Building Professional lawn care, landscaping, and property improvement in Northeast Arkansas. • lawn maintenance •lawn treatments and weed control • exterior projects • Custom landscape design & installation • Sod, trees, rock & drainage solutions • Residential & commercial services Reliable. Detailed. Done right.

Requirements
Must have
• Business name, service area, list of some of our services, clean design that represents
Nice to have
• Unique. Different design element than just grass because its already in n the logo. Picture of a warm season (south) lawn or landscape. Pictures of the type of work we do

```html
<!DOCTYPE html>
<html lang="en">
<head>
<meta charset="utf-8">
<title>Dorrin Yard and Building — Business Card</title>
<link href="https://fonts.googleapis.com/css2?family=Michroma&family=Arimo:wght@400;700&display=swap" rel="stylesheet">
<style>
  :root {
    --page-bg: #2a2a2a;
    --card-dark: #0b0b0b;
    --card-dark-glow: #2a2a2a;
    --card-light: #ffffff;
    --brand-green: #6ab23a;
    --text-light: #ffffff;
    --text-muted: #d6d6d6;
    --text-dark: #1c1c1c;
    --text-grey: #444444;
  }
  * { box-sizing: border-box; margin: 0; padding: 0; }
  html, body {
    width: 1200px; height: 800px; overflow: hidden;
    background: var(--page-bg);
  }
  .sheet {
    width: 1200px; height: 800px;
    display: flex; align-items: center; justify-content: center; gap: 40px;
  }
  .card {
    position: relative;
    width: 540px; height: 309px;
    border-radius: 18px;
    overflow: hidden;
    font-family: "Arimo", Arial, sans-serif;
  }

  /* Front */
  .card--front {
    background: radial-gradient(ellipse at 55% 40%, var(--card-dark-glow) 0%, var(--card-dark) 65%);
    color: var(--text-light);
  }
  .brand-mark {
    display: flex; align-items: center; gap: 10px;
    font-family: "Michroma", "Arimo", sans-serif;
    color: var(--brand-green);
    white-space: nowrap;
  }
  .brand-mark__dot {
    width: 18px; height: 18px; border-radius: 50%;
    background: var(--brand-green);
    flex-shrink: 0;
  }
  .card--front .brand-mark {
    position: absolute; left: 40px; top: 150px;
    font-size: 22px; letter-spacing: 1px;
  }
  .contact-block {
    position: absolute; right: 36px; top: 34px;
    text-align: right;
  }
  .owner-name {
    font-family: "Michroma", "Arimo", sans-serif;
    font-size: 22px; color: var(--brand-green);
    letter-spacing: 1px;
    white-space: nowrap;
  }
  .owner-role {
    margin-top: 4px;
    font-size: 14px; font-weight: 700; letter-spacing: 0.5px;
  }
  .phone {
    margin-top: 18px;
    display: flex; align-items: center; justify-content: flex-end; gap: 8px;
    font-size: 16px; font-weight: 700;
  }
  .icon-badge {
    width: 22px; height: 22px; border-radius: 50%;
    background: var(--brand-green);
    display: inline-flex; align-items: center; justify-content: center;
    flex-shrink: 0;
  }
  .website {
    position: absolute; left: 0; right: 0; bottom: 30px;
    text-align: center;
    font-size: 13px; letter-spacing: 1.2px; color: var(--text-muted);
  }

  /* Back */
  .card--back {
    background: var(--card-light);
    color: var(--text-dark);
  }
  .location {
    position: absolute; right: 24px; top: 22px;
    display: flex; align-items: center; gap: 8px;
    font-size: 13px; color: var(--text-grey);
    white-space: nowrap;
  }
  .card--back .brand-mark {
    position: absolute; left: 28px; top: 62px;
    font-size: 15px;
  }
  .company-title {
    position: absolute; left: 28px; top: 100px;
    font-family: "Michroma", "Arimo", sans-serif;
    font-size: 19px; font-weight: 400; color: var(--brand-green); letter-spacing: 0.5px;
    white-space: nowrap;
  }
  .services {
    position: absolute; left: 30px; top: 134px; right: 24px;
    list-style: none;
    font-size: 13.5px; line-height: 19px;
  }
  .services li { display: flex; gap: 8px; }
  .services li::before {
    content: ""; width: 5px; height: 5px; border-radius: 50%;
    background: var(--brand-green); margin-top: 7px; flex-shrink: 0;
  }
</style>
</head>
<body>
<main class="sheet">
  <section class="card card--front">
    <div class="brand-mark"><span class="brand-mark__dot"></span>DORRIN</div>
    <div class="contact-block">
      <p class="owner-name">MARCUS TOLLER</p>
      <p class="owner-role">OWNER</p>
      <p class="phone">(870) 555-0148
        <span class="icon-badge">
          <svg width="12" height="12" viewBox="0 0 12 12" aria-hidden="true">
            <rect x="3" y="1" width="6" height="10" rx="1.2" fill="none" stroke="#fff" stroke-width="1.3"/>
            <circle cx="6" cy="9" r="0.7" fill="#fff"/>
          </svg>
        </span>
      </p>
    </div>
    <p class="website">WWW.DORRINYARDANDBUILDING.EXAMPLE</p>
  </section>

  <section class="card card--back">
    <p class="location">Halden Springs, AR, United States, Arkansas
      <span class="icon-badge">
        <svg width="12" height="12" viewBox="0 0 12 12" aria-hidden="true">
          <path d="M6 11 C3 7.5 2.5 6 2.5 4.6 A3.5 3.5 0 0 1 9.5 4.6 C9.5 6 9 7.5 6 11 Z" fill="#fff"/>
          <circle cx="6" cy="4.6" r="1.3" fill="#6ab23a"/>
        </svg>
      </span>
    </p>
    <div class="brand-mark"><span class="brand-mark__dot"></span>DORRIN</div>
    <h1 class="company-title">DORRIN YARD AND BUILDING</h1>
    <ul class="services">
      <li>Dorrin Yard And Building Professional lawn care</li>
      <li>Landscaping and property improvement in Northeast Arkansas</li>
      <li>Lawn maintenance</li>
      <li>Lawn treatments and weed control</li>
      <li>Exterior projects</li>
      <li>Custom landscape design &amp; installation</li>
      <li>Sod, trees, rock &amp; drainage solutions</li>
      <li>Residential &amp; commercial services Reliable</li>
    </ul>
  </section>
</main>
</body>
</html>
```